Business Card Design Project

We need a business card design for a new construction company called 'KORVA HOLDINGS PTY.LTD' We run a construction based company for high end market homes in melbourne, we want something that looks professional and eye catching.The card needs to have a strong design to it something modern as the company name explains "korva." The final design should communicate professionalism and a strong image to our customers on the quality of our work.
On the business card i need
Name: Marek Holtvay
Mob:0417295031
Email:korva.holdings@mailbrook.example
Domestic/Residential/Commercial

```html
<!DOCTYPE html>
<html lang="en">
<head>
<meta charset="utf-8">
<title>Korva Holdings – Business Card</title>
<link rel="stylesheet" href="https://fonts.googleapis.com/css2?family=Bodoni+Moda:wght@400;600&family=Montserrat:wght@500;700&display=swap">
<style>
  :root {
    --canvas: #ffffff;
    --card: #272324;
    --ink-light: #ffffff;
    --accent: #e9a41d;
    --label: #1a1a1a;
    --photo-light: #dfe1ee;
    --photo-mid: #a9adc4;
  }
  * { margin: 0; padding: 0; box-sizing: border-box; }
  html, body { width: 1200px; height: 900px; overflow: hidden; background: var(--canvas); }
  .sheet { position: relative; width: 1200px; height: 900px; }

  .side-label {
    position: absolute;
    top: 24px;
    font-family: "Montserrat", Arial, sans-serif;
    font-weight: 500;
    font-size: 29px;
    color: var(--label);
  }
  .side-label--front { left: 56px; }
  .side-label--back { left: 504px; }

  .card {
    position: absolute;
    top: 62px;
    width: 411px;
    height: 717px;
    background: var(--card);
  }
  .card--front { left: 59px; }
  .card--back { left: 490px; top: 61px; }

  .hero-photo {
    position: absolute;
    left: 31px;
    top: 75px;
    width: 350px;
    height: 447px;
    background: linear-gradient(160deg, var(--photo-light) 0%, #c8cbde 45%, var(--photo-mid) 100%);
  }

  .brand {
    position: absolute;
    left: 41px;
    top: 528px;
    width: 332px;
    text-align: center;
    color: var(--ink-light);
    font-family: "Montserrat", Arial, sans-serif;
  }
  .brand__name {
    display: block;
    font-weight: 700;
    font-size: 96px;
    line-height: 1;
    letter-spacing: -2px;
  }
  .brand__legal {
    display: block;
    margin-top: 10px;
    font-weight: 700;
    font-size: 13px;
    letter-spacing: 5.2px;
    white-space: nowrap;
  }

  .contact {
    position: absolute;
    right: 54px;
    top: 38px;
    writing-mode: vertical-rl;
    font-family: "Bodoni Moda", "Times New Roman", serif;
    color: var(--ink-light);
    list-style: none;
  }
  .contact__item {
    font-size: 17px;
    line-height: 27px;
    white-space: nowrap;
  }
  .contact__item::before { content: "• "; }
  .contact__item--name {
    font-size: 25px;
    line-height: 34px;
    letter-spacing: 0.5px;
  }
  .contact__item--name::before { content: "•"; }
  .contact__item--phone { color: var(--accent); font-weight: 600; font-size: 18px; }
</style>
</head>
<body>
<main class="sheet">
  <span class="side-label side-label--front">Front</span>
  <span class="side-label side-label--back">reversed</span>

  <section class="card card--front">
    <div class="hero-photo" role="img" aria-label="Photo of a claw hammer, tape measure and nails lying on architectural blueprints"></div>
    <div class="brand">
      <span class="brand__name">korva</span>
      <span class="brand__legal">KORVA HOLDINGS PTY.LTD</span>
    </div>
  </section>

  <section class="card card--back">
    <ul class="contact">
      <li class="contact__item contact__item--name">Marek Holtvay</li>
      <li class="contact__item contact__item--phone">0417295031</li>
      <li class="contact__item">korva.holdings@mailbrook.example</li>
      <li class="contact__item">Domestic/Residential/Commercial</li>
    </ul>
  </section>
</main>
</body>
</html>
```